Integrative Medical Practice Website Redo

I am needing to have our current website redesigned to make it a responsive website to work on smartphones.
Current website
www.brightoakfm.com
Here are several examples of what I am looking for
https://www.corvanhealth.com/
I am wanting a popup for a newsletter signup
Looking for a very professional, clean, simple, minimalist, bold well designed website
Colors would ideally be greens and blues, cool tones, muted colors, or graytones like:
https://journeybright.org/
Several other clean design examples
http://7harborsrenton.com/
http://www.belvomedical.com/
http://sunpathyouth.com/
http://yourcellduke.com/
I would like the top navigation bar to be able to slide down while browsing site
We are also needing to add several features that are not on our current website:
Questionnaire buttons
Are you toxic questionnaire?
Take our hormone quiz to find out if hormones are affecting your health.
online scheduling option for:
nutrition counselling
testing like body composition, basal metabolic rate, CIMT, breast thermography, VO2 Max testing, Vita Trace
Therapies like whole body vibration, infrared sauna, Exercise with oxygen, hyperbaric oxygen, spinal decompression
Need to have separate page for different services and split up services into:
Consults/Office Visits, Testing, Therapies, Procedures
Need to have a button link to patient portal
Needs to have online store
Need to add navigation button "Start Here"
Need a spot for a video on practice summary
Newsletter signup to collect emails
Testimonials from linkpage
Blog that posts can be shared with social media
Password protected patient access that can integrate into crate.net ideally
Modules for programs online classes/videos
I have attached stock images that you can use, but feel free to find others to use.
I have also attached a copy of our current brochure that shows an overview of the practice
Target Market(s)
Health conscious people of all ages looking for a family medicine doctor
Industry/Entity Type
Alternative Medicine
Coding
Coded - Design and coding required
Number of Pages Required
5+ page
Look and feel

```html
<!DOCTYPE html>
<html lang="en">
<head>
<meta charset="utf-8">
<title>Bright Oak Family Medicine</title>
<link rel="stylesheet" href="https://fonts.googleapis.com/css2?family=Roboto:wght@300;400;500;700&family=Fredoka:wght@500;600&display=swap">
<style>
:root{
  --blue:#2a8fd4;
  --blue-btn:#35a3dc;
  --blue-tile:#2489d0;
  --green:#7db43a;
  --green-dark:#5d9a2a;
  --ink:#333;
  --muted:#666;
  --dark:#262626;
  --footer:#1d1d1d;
  --white:#fff;
}
*{box-sizing:border-box;margin:0;padding:0}
html,body{width:1200px;height:3030px;overflow:hidden}
body{position:relative;background:var(--white);font-family:'Roboto',sans-serif;color:var(--ink)}
.abs{position:absolute}
.center{text-align:center;left:0;width:1200px}

/* header */
.logo{position:absolute;display:flex;align-items:center;gap:10px}
.logo-dot{width:30px;height:30px;border-radius:50%;background:var(--green)}
.logo-name{font-family:'Roboto',sans-serif;font-weight:700;font-size:36px;color:var(--blue);line-height:1}
.logo-sub{font-size:11px;letter-spacing:4px;color:var(--blue);margin-top:3px}
.topbar{position:absolute;top:22px;left:605px;display:flex;align-items:center;gap:16px;font-size:13px;color:#444}
.topbar .item{display:flex;align-items:center;gap:10px}
.social-mini{width:16px;height:16px;border:1.5px solid #555;border-radius:50%}
.newsline{position:absolute;top:52px;left:770px;font-size:9px;color:#555}
.btn-sm{position:absolute;top:50px;left:903px;width:72px;height:20px;border-radius:10px;background:var(--blue-btn);color:#fff;font-size:9px;display:flex;align-items:center;justify-content:center}
.header-rule{position:absolute;top:92px;left:0;width:1200px;height:3px;background:var(--green)}
.nav{position:absolute;top:104px;left:288px;display:flex;gap:24px;font-size:11px;color:#333}
.nav .active{color:var(--green-dark);border-bottom:2px solid var(--green);padding-bottom:2px}

/* hero */
.hero{position:absolute;top:124px;left:0;width:1200px;height:342px;background:linear-gradient(180deg,#6b8aa6 0%,#9aa7ae 40%,#b8b0a8 70%,#8a7d74 100%)}
.hero-title{top:218px;font-family:'Fredoka',sans-serif;color:#fff;font-size:27px;font-weight:500}
.hero-title b{display:block;font-size:38px;font-weight:600;margin-top:2px}
.btn{position:absolute;border-radius:16px;background:var(--blue-btn);color:#fff;display:flex;align-items:center;justify-content:center;font-size:15px}

/* intro */
.section-title{color:var(--blue);font-weight:700;font-size:22px}
.intro-sub{top:527px;font-size:14px;color:#333}
.intro-text{top:590px;left:225px;width:345px;font-size:13.5px;line-height:23px;text-align:center;color:#333}
.video{top:572px;left:603px;width:365px;height:178px;background:linear-gradient(135deg,#7c6a5e,#c9b5a4 60%,#e7ddd3)}
.play{position:absolute;left:162px;top:69px;width:40px;height:40px;border:2px solid #fff;border-radius:50%}
.play::after{content:"";position:absolute;left:15px;top:11px;border-left:12px solid #fff;border-top:8px solid transparent;border-bottom:8px solid transparent}

/* lifestyle band */
.berry-band{top:858px;left:0;width:1200px;height:320px;background:linear-gradient(90deg,#9b2a35 0%,#6e1f27 35%,#4a2b24 60%,#3d3a20 100%)}
.berry-band::after{content:"";position:absolute;inset:0;background:rgba(0,0,0,.35)}
.habits{top:775px;left:198px;width:802px;height:163px;background:var(--green);display:flex;justify-content:space-around;padding:22px 20px 0;z-index:2}
.habit{width:140px;text-align:center;color:#fff;font-size:11px}
.habit-icon{width:94px;height:94px;border-radius:50%;background:#fff;margin:0 auto 12px;display:flex;align-items:center;justify-content:center}
.feedback-title{top:972px;color:#fff;font-size:22px;font-weight:700;z-index:2}
.avatar{top:1029px;left:252px;width:112px;height:112px;border-radius:50%;border:3px solid #fff;background:linear-gradient(160deg,#8d9aa5,#5d6770);z-index:2}
.quote{top:1025px;left:413px;width:560px;color:#fff;z-index:2;font-size:11.5px;line-height:22px}
.quote h3{font-size:15px;margin-bottom:4px;font-weight:700}
.arrow-c{width:28px;height:28px;border:1.5px solid #fff;border-radius:50%;z-index:2;top:1071px}

/* services */
.services-title{top:1212px}
.tile{position:absolute;width:153px;height:113px;background:var(--blue-tile);border-radius:8px;color:#fff;font-size:12.5px;line-height:19px;text-align:center;display:flex;flex-direction:column;align-items:center;justify-content:flex-end;padding-bottom:14px;box-shadow:0 3px 6px rgba(0,0,0,.15)}
.tile svg{margin-bottom:auto;margin-top:12px}

/* newsletter */
.newsletter{top:1587px;left:0;width:1200px;height:293px;background:linear-gradient(100deg,#2b2b2b,#4a4a45 45%,#262626)}
.nl-title{top:1618px;color:#fff;font-size:17px;font-weight:700}
.nl-text{top:1657px;left:240px;width:720px;color:#fff;font-size:13.5px;line-height:24px;text-align:center}
.nl-input{top:1722px;left:462px;width:276px;border-bottom:1px solid #ccc;color:#aaa;font-size:12px;text-align:center;padding-bottom:8px}

/* doctor */
.doc-photo{top:1836px;left:544px;width:112px;height:112px;border-radius:50%;border:4px solid #fff;background:linear-gradient(160deg,#b9c2c8,#7b8890);box-shadow:0 2px 6px rgba(0,0,0,.25)}
.doc-name{top:1970px;font-size:15px;font-weight:700;color:#333}
.doc-bio{top:1994px;font-size:10.5px;line-height:19px;color:#444}
.dots{top:2055px;left:574px;display:flex;gap:8px}
.dots i{width:6px;height:6px;border-radius:50%;border:1px solid var(--blue)}
.dots i:first-child{background:var(--blue)}

/* contact */
.contact{top:2105px;left:0;width:1200px;height:475px;background:linear-gradient(110deg,#2c2a27,#5b534a 50%,#7a6f63 75%,#3a3631)}
.contact::after{content:"";position:absolute;inset:0;background:rgba(0,0,0,.35)}
.contact-title{top:2130px;color:#fff;font-size:18px;font-weight:700;z-index:2}
.c-info{left:265px;color:#fff;z-index:2;display:flex;gap:16px;font-size:15px;font-weight:500}
.hours{top:2330px;left:308px;color:#fff;font-size:11.5px;line-height:23.5px;font-weight:500;z-index:2}
.field{position:absolute;left:622px;width:298px;border-bottom:1px solid #ddd;color:#bbb;font-size:13.5px;text-align:center;padding-bottom:8px;z-index:2}

/* map */
.map{top:2580px;left:0;width:1200px;height:205px;background:linear-gradient(180deg,#e9e6df,#dcd8ce)}

/* footer */
.footer{top:2785px;left:0;width:1200px;height:245px;background:var(--footer)}
.follow{top:2832px;left:268px;color:#9a9a9a;font-size:15px}
.soc{width:46px;height:46px;border:2px solid #8a8a8a;border-radius:50%;top:2818px}
.quick{top:2912px;color:#8a8a8a;font-size:14px}
.fnav{top:2950px;left:0;width:1200px;display:flex;justify-content:center;gap:26px;color:#7a7a7a;font-size:11px}
.copy{top:2983px;color:#6a6a6a;font-size:10px}
</style>
</head>
<body>

<header>
  <div class="logo" style="top:14px;left:230px">
    <span class="logo-dot"></span>
    <div><div class="logo-name">Bright Oak</div><div class="logo-sub">FAMILY MEDICINE</div></div>
  </div>
  <div class="topbar">
    <span class="item"><svg width="16" height="16" viewBox="0 0 24 24" fill="none" stroke="#444" stroke-width="2"><path d="M5 3h4l2 5-3 2a12 12 0 0 0 6 6l2-3 5 2v4a2 2 0 0 1-2 2A18 18 0 0 1 3 5a2 2 0 0 1 2-2z"/></svg>(555) 214-7730</span>
    <span class="item" style="margin-left:26px"><svg width="16" height="16" viewBox="0 0 24 24" fill="none" stroke="#444" stroke-width="2"><rect x="6" y="3" width="12" height="6"/><rect x="3" y="9" width="18" height="8" rx="1"/><rect x="7" y="14" width="10" height="7"/></svg>(555) 214-7731</span>
    <span class="social-mini" style="margin-left:26px"></span><span class="social-mini" style="margin-left:-10px"></span>
  </div>
  <div class="newsline">For newsletter subscribe here</div>
  <div class="btn-sm">Subscribe</div>
  <div class="header-rule"></div>
  <nav class="nav">
    <span class="active">HOME</span><span>ABOUT US</span><span>SERVICES</span><span>RESOURCES</span><span>ONLINE STORE</span><span>MEMBERS</span><span>FAQ'S</span><span>CONTACT US</span>
    <svg width="16" height="14" viewBox="0 0 24 20" fill="none" stroke="#333" stroke-width="2" style="margin-left:50px"><path d="M1 2h4l3 11h12l3-8H7"/><circle cx="9" cy="18" r="1.5"/><circle cx="19" cy="18" r="1.5"/></svg>
  </nav>
</header>

<section>
  <div class="hero" role="img" aria-label="Woman with arms raised outdoors against a bright sky"></div>
  <div class="abs center hero-title">Helping you to live a<b>Bright Oak</b></div>
  <div class="btn" style="top:335px;left:480px;width:238px;height:30px">Start Now</div>
</section>

<section>
  <div class="abs center section-title" style="top:497px">Restoring your Health Naturally with</div>
  <div class="abs center intro-sub">Nutrition, Manipulation, Acupuncture, and Integrative Medicine</div>
  <p class="abs intro-text">In our practice, we believe that prevention is the key to lifelong health and wellness. We are committed to helping you get well, stay well, and live well. It is our mission not only to heal, but to inspire and motivate our patients toembrace a healthy, active lifestyle.</p>
  <div class="abs video" role="img" aria-label="Practice summary video still of a man resting during a treatment"><span class="play"></span></div>
</section>

<section>
  <div class="abs berry-band" role="img" aria-label="Close-up of fresh strawberries"></div>
  <div class="abs habits">
    <div class="habit"><div class="habit-icon"><svg width="50" height="50" viewBox="0 0 50 50" fill="none" stroke="var(--green)" stroke-width="4"><circle cx="25" cy="25" r="21"/><rect x="11" y="23" width="28" height="5" fill="var(--green)" stroke="none"/><path d="M10 10l30 30"/></svg></div>No Smoking</div>
    <div class="habit"><div class="habit-icon"><svg width="54" height="44" viewBox="0 0 54 44" fill="var(--green)"><path d="M4 20h46a23 22 0 0 1-46 0z"/><circle cx="18" cy="14" r="7"/><circle cx="32" cy="12" r="8"/><circle cx="42" cy="16" r="5"/></svg></div>Healthy Eating</div>
    <div class="habit"><div class="habit-icon"><svg width="30" height="60" viewBox="0 0 30 60" fill="var(--green)"><circle cx="15" cy="7" r="6"/><path d="M5 16h20l3 22H20v20h-10V38H2z"/></svg></div>Healthy Weight</div>
    <div class="habit"><div class="habit-icon"><svg width="56" height="44" viewBox="0 0 56 44" fill="none" stroke="var(--green)" stroke-width="3.5"><circle cx="12" cy="32" r="9"/><circle cx="44" cy="32" r="9"/><path d="M12 32l10-14h14l8 14M22 18l8 14"/><circle cx="32" cy="6" r="4" fill="var(--green)"/></svg></div>Daily Exercise</div>
    <div class="habit"><div class="habit-icon"><svg width="56" height="46" viewBox="0 0 56 46" fill="var(--green)"><rect x="4" y="26" width="48" height="10"/><rect x="4" y="10" width="4" height="32"/><rect x="48" y="30" width="4" height="12"/><rect x="10" y="20" width="12" height="6" rx="3"/><text x="30" y="16" font-family="Roboto,sans-serif" font-size="14" font-weight="700">zz</text></svg></div>Adequate Sleep</div>
  </div>
  <div class="abs center feedback-title">Linkpage Feedback</div>
  <div class="abs avatar" role="img" aria-label="Portrait of a smiling patient in a suit"></div>
  <div class="abs quote"><h3>Lorem Ipsum</h3>Lorem Ipsum is simply dummy text of the printing and typesetting industry. Lorem Ipsum has been the industry's standard dummy text ever since the 1500s, when an unknown printer took a galley of type and scrambled it to make a type specimen book. It has survived not only five centuries, but also the leap into electronic typesetting, remaining essentially unchanged</div>
  <svg class="abs arrow-c" style="left:199px" viewBox="0 0 28 28" fill="none" stroke="#fff" stroke-width="1.5"><path d="M16 9l-5 5 5 5"/></svg>
  <svg class="abs arrow-c" style="left:972px" viewBox="0 0 28 28" fill="none" stroke="#fff" stroke-width="1.5"><path d="M12 9l5 5-5 5"/></svg>
</section>

<section>
  <div class="abs center section-title services-title">Our Services</div>
  <div class="tile" style="top:1272px;left:227px"><svg width="40" height="40" viewBox="0 0 40 40" fill="none" stroke="#fff" stroke-width="2.5"><path d="M20 14c-3-6-12-4-10 3 1 4 10 10 10 10s9-6 10-10c2-7-7-9-10-3z"/><path d="M4 24l8 8h10M36 24l-8 8H18"/></svg>INTEGRATIVE FAMILY<br>MEDICINE</div>
  <div class="tile" style="top:1272px;left:421px"><svg width="40" height="40" viewBox="0 0 40 40" fill="none" stroke="#fff" stroke-width="2.5"><rect x="8" y="4" width="18" height="24"/><path d="M12 10h10M12 15h10"/><path d="M14 28a10 8 0 0 0 20 0z"/></svg>NUTRITION</div>
  <div class="tile" style="top:1272px;left:615px"><svg width="40" height="40" viewBox="0 0 40 40" fill="none" stroke="#fff" stroke-width="2.5"><circle cx="10" cy="24" r="5"/><path d="M14 21l16-12M14 27l16 8"/><circle cx="32" cy="8" r="3"/></svg>OSTEOPATHIC<br>MANIPULATION</div>
  <div class="tile" style="top:1272px;left:809px"><svg width="40" height="40" viewBox="0 0 40 40" fill="none" stroke="#fff" stroke-width="2.5"><rect x="8" y="4" width="24" height="32" rx="2"/><circle cx="20" cy="20" r="6"/></svg>ALLERGY TESTING<br>&amp; TREATMENT</div>
  <div class="tile" style="top:1423px;left:227px"><svg width="40" height="40" viewBox="0 0 40 40" fill="none" stroke="#fff" stroke-width="2.5"><rect x="14" y="3" width="12" height="6"/><rect x="9" y="9" width="22" height="28" rx="3"/><path d="M20 16v14M13 23h14"/></svg>FUNCTIONAL<br>MEDICINE</div>
  <div class="tile" style="top:1423px;left:421px"><svg width="40" height="40" viewBox="0 0 40 40" fill="none" stroke="#fff" stroke-width="2.5"><path d="M6 14h28v12H6zM12 14v5M18 14v5M24 14v5M30 14v5"/></svg>WEIGHT LOSS</div>
  <div class="tile" style="top:1423px;left:615px"><svg width="40" height="40" viewBox="0 0 40 40" fill="none" stroke="#fff" stroke-width="2"><path d="M14 4l4 32M20 4v32M26 4l-4 32"/></svg>ACUPUNCTURE</div>
  <div class="tile" style="top:1423px;left:809px"><svg width="40" height="40" viewBox="0 0 40 40" fill="none" stroke="#fff" stroke-width="2.5"><rect x="8" y="4" width="24" height="32" rx="2"/><path d="M16 12l8 16M24 12l-8 16"/></svg>OTHER TESTING<br>&amp; THERAPIES</div>
</section>

<section>
  <div class="abs newsletter" role="img" aria-label="Hands holding a young plant seedling"></div>
  <div class="abs center nl-title">Subscribe For Newsletter</div>
  <p class="abs nl-text">Lorem Ipsum is simply dummy text of the printing and typesetting industry. Lorem Ipsum has been the industry's standard dummy text ever since the 1500s</p>
  <div class="abs nl-input">Enter your email address here</div>
  <div class="btn" style="top:1770px;left:478px;width:238px;height:30px">Subscribe</div>
</section>

<section>
  <div class="abs doc-photo" role="img" aria-label="Portrait of the practice physician"></div>
  <div class="abs center doc-name">Dr Marlowe</div>
  <p class="abs center doc-bio">Dr Marlowe was born and raised in Texas. Early on, his exposure to medicine came from EMT and surgery tech training to<br>seminars on nutrition, homeopathy, manipulation and acupuncture with his father (a chiropractor).</p>
  <div class="abs dots"><i></i><i></i><i></i><i></i></div>
</section>

<section>
  <div class="abs contact" role="img" aria-label="Smiling couple embracing outdoors"></div>
  <div class="abs center contact-title">Contact Us</div>
  <div class="abs c-info" style="top:2193px"><svg width="20" height="20" viewBox="0 0 24 24" fill="none" stroke="#fff" stroke-width="2"><path d="M5 3h4l2 5-3 2a12 12 0 0 0 6 6l2-3 5 2v4a2 2 0 0 1-2 2A18 18 0 0 1 3 5a2 2 0 0 1 2-2z"/></svg>(555) 214-7730</div>
  <div class="abs c-info" style="top:2237px"><svg width="20" height="20" viewBox="0 0 24 24" fill="none" stroke="#fff" stroke-width="2"><rect x="6" y="3" width="12" height="6"/><rect x="3" y="9" width="18" height="8" rx="1"/><rect x="7" y="14" width="10" height="7"/></svg>(555) 214-7731</div>
  <div class="abs c-info" style="top:2280px;line-height:20px"><svg width="20" height="20" viewBox="0 0 24 24" fill="none" stroke="#fff" stroke-width="2"><rect x="6" y="3" width="12" height="6"/><rect x="3" y="9" width="18" height="8" rx="1"/><rect x="7" y="14" width="10" height="7"/></svg><span>482 Harlow Lane,<br>Cedar Vale, TX 70114</span></div>
  <div class="abs hours">Work Hours:<br>Monday ( 8 am - 6 pm ),<br>Tuesd ( 8 am - 6 pm ),<br>Wednesday ( 9 am - 6 pm ),<br>Thursday ( 8 am - 4 pm ),<br>Friday ( 9 am - 1 pm )<br>( The office is closed from 12-1 for lunch )</div>
  <div class="field" style="top:2185px">Your Name</div>
  <div class="field" style="top:2238px">Email Id</div>
  <div class="field" style="top:2292px">Phone No</div>
  <div class="field" style="top:2346px">Subject</div>
  <div class="field" style="top:2398px;height:76px">Message</div>
  <div class="btn" style="top:2515px;left:650px;width:238px;height:30px;z-index:2">Subscribe</div>
</section>

<div class="abs map" role="img" aria-label="Street map showing the office location"></div>

<footer>
  <div class="abs footer"></div>
  <div class="abs follow">Follow us</div>
  <span class="abs soc" style="left:372px"></span>
  <span class="abs soc" style="left:435px"></span>
  <span class="abs soc" style="left:498px"></span>
  <div class="logo" style="top:2820px;left:700px">
    <span class="logo-dot" style="background:#666"></span>
    <div><div class="logo-name" style="color:#666">Bright Oak</div><div class="logo-sub" style="color:#666">FAMILY MEDICINE</div></div>
  </div>
  <div class="abs center quick">Quick Links</div>
  <div class="abs fnav"><span>HOME</span><span>ABOUT US</span><span>SERVICES</span><span>RESOURCES</span><span>ONLINE STORE</span><span>MEMBERS</span><span>FAQ'S</span><span>CONTACT US</span></div>
  <div class="abs center copy">© 2016 Bright Oak. All Rights Reserved.</div>
</footer>

</body>
</html>
```